Clean, creative business Wordpress Site

Our company is building a website via Wordpress and needs a clean, no fuss, modern looking design that reflects our company brand (see attached logos).

In addition, the company is a woman owned business (no middle-aged white guy stock photos please) and primarily works with the oil & gas industry. We would prefer no images with direct references to energy (rigs, windmills, solar panels, etc.). Part of our consulting is providing thought leadership around energy politics and policy so creative ways to incorporate that visually will be appreciated as well.

Site map of pages below:

Home
- About
- Team
- Expertise
- Blog

We prefer a header image that includes the company logo and easy to identify and navigate menus.

Target Market(s)

Energy professionals, Executives

Industry/Entity Type

Consulting

Font styles to use
Serif

Colors
85acd3
0255a3
cedeed
ffffff

Requirements
Must have
• Clean and easy to navigate, clear menus, simple design that reflects company logo.

```html
<!DOCTYPE html>
<html lang="en">
<head>
<meta charset="utf-8">
<title>Corvantis Energy</title>
<link href="https://fonts.googleapis.com/css2?family=Cinzel:wght@400;700&family=Open+Sans:wght@400;600;700&family=Raleway:wght@600;700&display=swap" rel="stylesheet">
<style>
:root{
  --blue:#0255a3;
  --blue-mid:#1f5f9e;
  --blue-light:#85acd3;
  --blue-pale:#cedeed;
  --white:#ffffff;
  --ink:#2b2b2b;
  --text:#555555;
  --muted:#999999;
  --grey-band:#f2f2f2;
  --footer:#1b1b1b;
  --serif:'Cinzel', serif;
  --sans:'Open Sans', sans-serif;
}
*{box-sizing:border-box;margin:0;padding:0}
html,body{width:1200px;height:2765px;overflow:hidden;background:var(--white)}
body{position:relative;font-family:var(--sans);color:var(--text)}
.abs{position:absolute}
.section{position:absolute;left:0;width:1200px}

/* header */
.site-header{top:0;height:88px;background:var(--white);border-top:4px solid var(--blue)}
.brand{left:162px;top:18px;display:flex;align-items:center;gap:12px}
.brand-mark{width:46px;height:46px;border-radius:50%;background:var(--blue)}
.brand-name{font-family:var(--serif);font-size:28px;color:var(--blue);letter-spacing:1px}
.topbar{left:719px;top:0;width:319px;height:32px;background:var(--blue);clip-path:polygon(0 0,100% 0,94% 100%,6% 100%);display:flex;align-items:center;justify-content:center;gap:18px;font-size:11px;color:var(--white)}
.topbar span{display:flex;align-items:center;gap:6px}
.main-nav{top:52px;left:0;width:1200px;font-size:12px;color:var(--ink)}
.main-nav a{position:absolute;text-decoration:none;color:var(--ink)}
.main-nav a.active{color:var(--blue);font-weight:600}
.main-nav .sep{position:absolute;top:-2px;width:1px;height:18px;background:#ddd}

/* hero */
.hero{top:88px;height:487px}
.hero-photo{position:absolute;inset:0;background:linear-gradient(135deg,#3b3f45 0%,#6b6f74 45%,#4a4c50 70%,#2c2e31 100%)}
.hero-shade{position:absolute;inset:0;background:linear-gradient(90deg,rgba(0,0,0,0) 40%,rgba(0,0,0,.35) 100%)}
.hero-arrow{position:absolute;left:98px;top:231px;width:26px;height:26px;border:1px solid rgba(255,255,255,.8)}
.hero-copy{position:absolute;right:162px;top:318px;text-align:right;color:var(--white);width:560px}
.hero-title{font-family:'Raleway',sans-serif;font-weight:700;font-size:37px;letter-spacing:.5px}
.hero-text{font-size:13px;line-height:20px;margin-top:8px}
.btn{display:inline-block;background:var(--blue-mid);color:var(--white);font-size:12px;text-align:center;border-radius:2px}
.hero-btn{position:absolute;left:763px;top:419px;width:113px;height:30px;line-height:30px}

/* about */
.about{top:575px;height:323px}
.about-brand{left:162px;top:110px;width:240px;text-align:center}
.about-brand .mark{width:74px;height:74px;border-radius:50%;background:var(--blue);margin:0 auto 12px}
.about-brand .name{font-family:var(--serif);font-size:28px;color:var(--blue)}
.about-rule{left:415px;top:48px;width:2px;height:230px;background:var(--blue-pale)}
.section-title{font-family:var(--serif);font-size:29px;color:var(--ink);letter-spacing:1px}
.section-title em{font-style:normal;color:var(--blue)}
.about-title{left:439px;top:44px}
.about-text{left:439px;top:108px;width:600px;font-size:11.5px;line-height:28px}
.about-btn{left:439px;top:245px;width:112px;height:30px;line-height:30px}

/* centred headings */
.center-title{position:absolute;left:0;width:1200px;text-align:center}
.title-rule{position:absolute;left:570px;width:60px;height:2px;background:var(--blue)}

/* expertise */
.expertise{top:898px;height:494px;background:var(--grey-band)}
.skill{position:absolute;width:270px;text-align:center}
.skill svg{display:block;margin:0 auto 8px}
.skill h3{font-family:var(--serif);font-size:14px;color:var(--ink);font-weight:700;line-height:18px;font-variant:small-caps}
.skill p{font-size:11px;line-height:18px;margin-top:6px;color:var(--text)}
.skill .rule{width:240px;height:1px;background:#ddd;margin:12px auto 0}
.expert-photo{position:absolute;left:507px;top:230px;width:190px;height:264px;background:linear-gradient(180deg,#d9d6d2 0%,#b9b3ad 50%,#8a8f96 100%);border-radius:40px 40px 0 0}

/* team */
.team{top:1392px;height:381px}
.member{position:absolute;top:105px;width:195px}
.member-photo{width:195px;height:186px;background:linear-gradient(160deg,#8fa6bd 0%,#5d6b78 55%,#2f3338 100%)}
.member-card{position:absolute;left:10px;top:138px;width:175px;height:46px;background:rgba(255,255,255,.92);text-align:center;padding-top:6px}
.member-card h4{font-family:var(--serif);font-size:15px;color:var(--ink);font-weight:400;letter-spacing:.5px}
.member-card span{font-size:10px;color:var(--muted)}
.member.featured .member-card h4{color:var(--blue)}
.member-social{margin:6px 10px 0;height:30px;background:#f0f0f0;display:flex;justify-content:center;align-items:center;gap:18px}
.member-social i{width:9px;height:9px;background:#444;border-radius:50%;display:block}
.team-arrow{position:absolute;top:217px;width:26px;height:26px;border:1px solid #bbb;background:var(--white)}

/* testimonial */
.testimonial{top:1773px;height:260px;background:var(--grey-band)}
.quote-mark{left:160px;top:120px;font-family:Georgia,serif;font-size:80px;line-height:60px;color:var(--blue);font-weight:700}
.quote-text{left:223px;top:106px;width:480px;font-size:11.5px;line-height:18px;color:var(--text)}
.quote-author{left:223px;top:197px;font-family:var(--serif);font-size:13px;color:var(--muted)}
.quote-author b{color:var(--blue)}
.quote-rule{left:728px;top:110px;width:1px;height:100px;background:#ccc}
.avatar{position:absolute;top:104px;width:80px;height:80px;border-radius:50%;background:linear-gradient(180deg,#c9b7a6,#6f7b87);border:3px solid var(--white);box-shadow:0 0 0 1px #ccc}
.avatar.active{box-shadow:0 0 0 2px var(--blue)}
.dots{left:866px;top:204px;display:flex;gap:6px}
.dots i{width:9px;height:9px;border-radius:50%;border:1px solid var(--blue);display:block}
.dots i.on{background:var(--blue-light)}

/* blog */
.blog{top:2033px;height:442px}
.post{position:absolute;top:107px;width:421px}
.post-photo{width:421px;height:188px;border:3px solid #ddd}
.post-date{position:absolute;left:0;top:212px;width:44px;text-align:center}
.post-date .day{background:#e6e6e6;height:30px;line-height:30px;font-size:15px;color:var(--ink)}
.post-date .mon{background:var(--blue);height:27px;line-height:27px;font-size:11px;color:var(--white);font-weight:700}
.post-body{position:absolute;left:68px;top:214px;width:350px}
.post-body h4{font-family:var(--serif);font-size:14px;color:var(--ink);font-weight:700}
.post-body p{font-size:10.5px;line-height:16px;margin-top:4px}
.post-meta{font-size:9.5px;color:var(--muted);margin-top:8px;display:flex;gap:16px}

/* footer */
.site-footer{top:2475px;height:253px;background:var(--footer);color:#cfcfcf}
.foot-col{position:absolute;top:44px}
.foot-col h5{font-size:13px;color:var(--white);font-weight:700;padding-bottom:10px;border-bottom:1px solid #444;width:240px}
.foot-col h5 em{font-style:normal;color:var(--blue-light)}
.foot-links{list-style:none;font-size:11px;line-height:30px;margin-top:6px}
.foot-contact{font-size:11px;line-height:18px;margin-top:10px}
.foot-contact b{color:var(--white)}
.foot-contact .row{display:flex;align-items:center;gap:10px;margin-top:10px}
.foot-map{position:absolute;left:0;top:38px;width:262px;height:137px;background:linear-gradient(135deg,#c9d7c4,#a8c2d8 60%,#d9d2b8);border:3px solid #ddd}
.foot-brand{left:881px;top:92px;width:160px;text-align:center}
.foot-brand .mark{width:40px;height:40px;border-radius:50%;background:#999;margin:0 auto 8px}
.foot-brand .name{font-family:var(--serif);font-size:20px;color:#cfcfcf}
.foot-social{display:flex;gap:6px;justify-content:center;margin-top:18px}
.foot-social i{width:24px;height:24px;border-radius:50%;background:var(--blue-light);display:block}
.copyright{top:2728px;height:37px;background:var(--blue-mid);color:var(--white);font-size:11px;text-align:center;line-height:37px}
</style>
</head>
<body>

<header class="section site-header">
  <div class="abs brand"><span class="brand-mark"></span><span class="brand-name">Corvantis Energy</span></div>
  <div class="abs topbar">
    <span><svg width="10" height="10" viewBox="0 0 10 10"><path d="M2 1l2 2-1 1.5c.6 1.2 1.3 1.9 2.5 2.5L7 6l2 2-1.5 1.5C4 9 1 6 .5 2.5z" fill="#fff"/></svg>123-456-7890</span>
    <span><svg width="11" height="8" viewBox="0 0 11 8"><rect width="11" height="8" fill="#fff"/><path d="M0 0l5.5 4.5L11 0" stroke="#0255a3" fill="none"/></svg>info@corvantisenergy.com</span>
  </div>
  <nav class="abs main-nav">
    <a class="active" style="left:564px">Home</a>
    <span class="sep" style="left:624px"></span>
    <a style="left:653px">About Us ▾</a>
    <span class="sep" style="left:741px"></span>
    <a style="left:770px">Expertise ▾</a>
    <span class="sep" style="left:857px"></span>
    <a style="left:889px">Our Team ▾</a>
    <span class="sep" style="left:983px"></span>
    <a style="left:1013px">Blog</a>
  </nav>
</header>

<section class="section hero">
  <div class="hero-photo" role="img" aria-label="Photo from above of business people around a table assembling large jigsaw puzzle pieces"></div>
  <div class="hero-shade"></div>
  <div class="hero-arrow"><svg width="24" height="24" viewBox="0 0 24 24"><path d="M14 8l-4 4 4 4" stroke="#fff" stroke-width="1.5" fill="none"/></svg></div>
  <div class="hero-copy">
    <h1 class="hero-title">EXPERIENCE GREAT SERVICE</h1>
    <p class="hero-text">Lorem ipsum dolor s nonummy nibh euit amet, consectetuerg elit, sed<br>ismod tincidunt ut laoreet dolore magna aliquam erat.</p>
    <a class="btn hero-btn">READ MORE</a>
  </div>
</section>

<section class="section about">
  <div class="abs about-brand"><div class="mark"></div><div class="name">Corvantis Energy</div></div>
  <div class="abs about-rule"></div>
  <h2 class="abs section-title about-title">ABOUT <em>CORVANTIS ENERGY</em></h2>
  <p class="abs about-text">Lorem ipsum dolor sit amet, consectetuer adipiscing elit, sed diam nonummy nibh euismod tincidunt ut laoreet dolore magna aliquam erat volutpat. Ut wisi enim ad minim veniam, quis nostrud exerci tation ullamcorper suscipit lobortis nisl ut aliquip ex ea commodo consequat. Duis autem vel eum iriure dolor in hendrerit in vulputate velit esse molestie consequat, vel illum dolore eu feugiat nulla facilisis at vero eros et accumsan et iusto odio dignissim qui blandit praesent luptatum zzril delenit augue duis dolore te feugait nulla facilisi.</p>
  <a class="abs btn about-btn">Read More</a>
</section>

<section class="section expertise">
  <h2 class="center-title section-title" style="top:40px">WE ARE <em>EXPERTISE IN</em></h2>
  <div class="title-rule" style="top:82px"></div>

  <div class="skill" style="left:465px;top:104px">
    <svg width="26" height="26" viewBox="0 0 26 26"><path d="M14 3l-6 11h5l-2 9 7-12h-5z" fill="none" stroke="#0255a3" stroke-width="1.6"/></svg>
    <h3>Descalating Conflict</h3>
    <p>Lorem ipsum dolor sit amet, consectetuer adipiscing elit, sed diam nonummy nibh euismod</p>
  </div>

  <div class="skill" style="left:160px;top:198px">
    <svg width="26" height="30" viewBox="0 0 26 30"><rect x="5" y="2" width="16" height="24" fill="#0255a3"/><path d="M8 9h10M8 13h10M8 17h10" stroke="#fff"/></svg>
    <h3>Navigating Policy</h3>
    <p>Lorem ipsum dolor sit amet, consectetuer adipiscing elit, sed diam nonummy nibh euismod</p>
    <div class="rule"></div>
  </div>
  <div class="skill" style="left:160px;top:346px">
    <svg width="40" height="26" viewBox="0 0 40 26"><path d="M3 10l9-5 8 5 8-5 9 5-9 10-8-4-8 4z" fill="#0255a3"/></svg>
    <h3>Community Engagement</h3>
    <p>Lorem ipsum dolor sit amet, consectetuer adipiscing elit, sed diam nonummy nibh euismod</p>
    <div class="rule"></div>
  </div>

  <div class="expert-photo" role="img" aria-label="Photo of two business colleagues standing and reviewing a document"></div>

  <div class="skill" style="left:777px;top:198px">
    <svg width="30" height="30" viewBox="0 0 30 30"><circle cx="15" cy="15" r="12" fill="none" stroke="#0255a3" stroke-width="1.8"/><path d="M16 7l-5 9h4l-1 7 5-9h-4z" fill="#0255a3"/></svg>
    <h3>Energy Access –<br>Reducing Energy Poverty</h3>
    <p>Lorem ipsum dolor sit amet, consectetuer adipiscing elit, sed diam nonummy nibh euismod</p>
    <div class="rule"></div>
  </div>
  <div class="skill" style="left:777px;top:334px">
    <svg width="30" height="34" viewBox="0 0 30 34"><path d="M8 6h14l-3 5v2a10 10 0 1 1-8 0v-2z" fill="none" stroke="#0255a3" stroke-width="1.8"/><circle cx="15" cy="23" r="3" fill="#0255a3"/></svg>
    <h3>Investor Relations</h3>
    <p>Lorem ipsum dolor sit amet, consectetuer adipiscing elit, sed diam nonummy nibh euismod</p>
    <div class="rule"></div>
  </div>
</section>

<section class="section team">
  <h2 class="center-title section-title" style="top:36px">OUR <em>TEAM</em></h2>
  <div class="title-rule" style="top:78px"></div>
  <div class="team-arrow" style="left:98px"><svg width="24" height="24" viewBox="0 0 24 24"><path d="M14 8l-4 4 4 4" stroke="#555" stroke-width="1.5" fill="none"/></svg></div>
  <div class="team-arrow" style="left:1075px"><svg width="24" height="24" viewBox="0 0 24 24"><path d="M10 8l4 4-4 4" stroke="#555" stroke-width="1.5" fill="none"/></svg></div>

  <div class="member" style="left:162px">
    <div class="member-photo" role="img" aria-label="Portrait photo of the founder in a dark suit"></div>
    <div class="member-card"><h4>Daniel Hart</h4><span>Founder &amp; Ceo</span></div>
    <div class="member-social"><i></i><i></i><i></i><i></i></div>
  </div>
  <div class="member featured" style="left:389px">
    <div class="member-photo" role="img" aria-label="Portrait photo of the administrator in a vest and tie"></div>
    <div class="member-card"><h4>Owen Reyes</h4><span>Administrator</span></div>
    <div class="member-social"><i></i><i></i><i></i><i></i></div>
  </div>
  <div class="member" style="left:616px">
    <div class="member-photo" role="img" aria-label="Portrait photo of the chief marketing officer in a tan jacket"></div>
    <div class="member-card"><h4>Peter Lindqvist</h4><span>Chief Marketing Officer</span></div>
    <div class="member-social"><i></i><i></i><i></i><i></i></div>
  </div>
  <div class="member" style="left:842px">
    <div class="member-photo" role="img" aria-label="Portrait photo of the chief marketing officer in a dark blazer"></div>
    <div class="member-card"><h4>Clara Bennett</h4><span>Chief Marketing Officer</span></div>
    <div class="member-social"><i></i><i></i><i></i><i></i></div>
  </div>
</section>

<section class="section testimonial">
  <h2 class="center-title section-title" style="top:36px">CLIENT <em>TESTIMONIAL</em></h2>
  <div class="title-rule" style="top:78px"></div>
  <div class="abs quote-mark">&ldquo;</div>
  <p class="abs quote-text">"Lorem ipsum dolor sit amet, consectetuer adipiscing elit, sed diam nonummy nibh euismod tincidunt ut laoreet dolore magna aliquam erat volutpat. Ut wisi enim ad minim veniam, quis nostrud exerci tation ullamcorper suscipit lobortis nisl ut aliquip ex ea commodo consequat. Duis autem vel eum."</p>
  <div class="abs quote-author"><b>Marisa,</b> Office Manager</div>
  <div class="abs quote-rule"></div>
  <div class="avatar" style="left:747px" role="img" aria-label="Client portrait photo"></div>
  <div class="avatar active" style="left:852px" role="img" aria-label="Client portrait photo"></div>
  <div class="avatar" style="left:957px" role="img" aria-label="Client portrait photo"></div>
  <div class="abs dots"><i></i><i class="on"></i><i></i></div>
</section>

<section class="section blog">
  <h2 class="center-title section-title" style="top:36px">LATEST <em>NEWS &amp; BLOG</em></h2>
  <div class="title-rule" style="top:78px"></div>

  <article class="post" style="left:162px">
    <div class="post-photo" role="img" aria-label="Photo of a hand moving a chess piece on a board" style="background:linear-gradient(180deg,#9a9a9a,#d8d8d8 60%,#5a5a5a)"></div>
    <div class="post-date"><div class="day">29</div><div class="mon">DEC</div></div>
    <div class="post-body">
      <h4>Lorem ipsum dolor sit amet.</h4>
      <p>Lorem ipsum dolor sit amet, consectetuer adipiscing elit, sed diam nonuy nibh volutpat veniam.... [ + ]</p>
      <div class="post-meta"><span>Sam Archer</span><span>Blog</span><span>1 Comments</span></div>
    </div>
  </article>
  <article class="post" style="left:619px">
    <div class="post-photo" role="img" aria-label="Photo of a row of red game pieces with one blue piece standing out" style="background:linear-gradient(180deg,#f1f1f1,#e6e6e6 50%,#c98080 75%,#e0e0e0)"></div>
    <div class="post-date"><div class="day">29</div><div class="mon">DEC</div></div>
    <div class="post-body">
      <h4>Lorem ipsum dolor sit amet.</h4>
      <p>Lorem ipsum dolor sit amet, consectetuer adipiscing elit, sed diam nonuy nibh volutpat veniam.... [ + ]</p>
      <div class="post-meta"><span>Sam Archer</span><span>Blog</span><span>1 Comments</span></div>
    </div>
  </article>
</section>

<footer class="section site-footer">
  <div class="foot-col" style="left:162px">
    <h5 style="width:120px">QUICK <em>LINKS</em></h5>
    <ul class="foot-links"><li>• Home</li><li>• About Us</li><li>• Expertise</li><li>• Our Team</li><li>• Blog</li></ul>
  </div>
  <div class="foot-col" style="left:321px">
    <h5 style="width:215px">CONTACT <em>INFORMATION</em></h5>
    <div class="foot-contact">
      <b>Corvantisenergy</b><br>Lorem ipsum dolor sit amet,<br>consectetuer dolor ut laoreet.
      <div class="row"><svg width="11" height="11" viewBox="0 0 10 10"><path d="M2 1l2 2-1 1.5c.6 1.2 1.3 1.9 2.5 2.5L7 6l2 2-1.5 1.5C4 9 1 6 .5 2.5z" fill="#ccc"/></svg>123.456.7890</div>
      <div class="row"><svg width="11" height="11" viewBox="0 0 11 11"><rect x="1" y="4" width="9" height="5" fill="#ccc"/><rect x="3" y="1" width="5" height="3" fill="#ccc"/></svg>123.456.7890</div>
      <div class="row"><svg width="11" height="8" viewBox="0 0 11 8"><rect width="11" height="8" fill="#ccc"/><path d="M0 0l5.5 4.5L11 0" stroke="#1b1b1b" fill="none"/></svg>info@corvantisenergy.com</div>
    </div>
  </div>
  <div class="foot-col" style="left:577px">
    <h5 style="width:262px">LOCATION <em>MAP</em></h5>
    <div class="foot-map" role="img" aria-label="Street map of the office location"></div>
  </div>
  <div class="abs foot-brand">
    <div class="mark"></div>
    <div class="name">Corvantis Energy</div>
    <div class="foot-social"><i></i><i></i><i></i><i style="background:#e0a040"></i></div>
  </div>
</footer>
<div class="section copyright">Copyright Corvantisenergy.com. All Right Reserved.</div>

</body>
</html>
```